Hand Sanitizer Bottle Labels for new product launch

We are a small, U.S. based, family-owned paint company that has converted some of our capacity to make sanitizer to help out during the shortages related to the COVID-19 pandemic. Our product is bio-based (made from U.S.-grown corn), super clear and clean! It will be marketed to schools, businesses and other customers in the U.S.

We need help THIS WEEKEND to design product labels in a few basic sizes for pails/drums (label size 8.5x14"), round gallon jugs (like windshield washer fluid, label size 6.25x10"), round quarts (label size 5x11"), and 8oz (label size 5x7") and 6 ounce cylindrical bottles (label size 3x7", for samples). A portion (a third?) of the label on the right will need to be used for ingredient and warning text. We are looking for a design for the one gallon jug size for evaluation. Once a design concept (and designer) is chosen, that design will be scaled/reconfigured into the different sizes shown above.

We would like the design to communicate: simple, clean, fresh, natural -- and would prefer to use green and/or yellow primary colors in the design due to the bio-based focus.

Major features to highlight on packaging:
- 80% ethyl alcohol
- Bio-based
- Made in the USA (could use a graphic for this)
- QRV approved formula (could use a graphic for this)
- Kills most germs and bacteria

In small text, we would like to include the text: "QRV Registration 7162093418" somewhere on the label.

For examples of competitive labels, image search: "QRV hand sanitizer brands".

Files attached: brand logo, pic of some of the bottles to be labeled, Word doc showing our initial sample label which includes the QRV-required text.

Target Market(s)

American consumers of all ages

Font styles to use
Serif
Sans Serif

Colors
0a90cc
85cae6
00a990
86cfc6
cfeae6
d9e8a8
acd036
fbed22
fbee3f

Requirements
Must have
• Clean, fresh look - suitable for us on clear or white stock labels. Graphics to quickly communicate key features: QRV approved formula, Made in the USA, Bio-Based. Must include all required warning and descriptive text as shown on the sample label. Proportions of label must be able to conform to the label sizes mentioned in the summary above.
Nice to have
• Prefer use of greens, blues or yellows to communicate the product's clean and natural ingredients.

```html
<!DOCTYPE html>
<html lang="en">
<head>
<meta charset="utf-8">
<title>Hollow Creek Hand Sanitizer – Gallon Label</title>
<link rel="stylesheet" href="https://fonts.googleapis.com/css2?family=Rubik:ital,wght@0,500;0,700;0,800;0,900;1,800;1,900&family=Oswald:wght@400&display=swap">
<style>
  :root {
    --leaf-light: #d3e08a;
    --leaf: #5a9a2a;
    --leaf-deep: #2f6e1a;
    --forest: #1f5a1c;
    --sun: #f6dc0a;
    --sun-deep: #d4bd00;
    --spark: #e08a10;
    --ink: #1c1c1c;
    --teal: #1f6f74;
    --alert-red: #d62030;
    --paper: #ffffff;
    --paper-shade: #ececec;
    --page: #ffffff;
  }
  html, body {
    margin: 0;
    width: 1200px;
    height: 1200px;
    overflow: hidden;
    background: var(--page);
  }
  .canvas {
    position: relative;
    width: 1200px;
    height: 1200px;
  }
  .label {
    position: absolute;
    left: 270px;
    top: 38px;
    width: 660px;
    height: 1123px;
    display: block;
  }
  .brand-name { font-family: "Rubik", sans-serif; font-weight: 800; fill: var(--paper); }
  .headline { font-family: "Rubik", sans-serif; font-weight: 900; font-style: italic; fill: var(--leaf); stroke: var(--forest); stroke-width: 2.5; paint-order: stroke; }
  .strength { font-family: "Oswald", sans-serif; font-weight: 400; fill: var(--ink); }
  .bio { font-family: "Rubik", sans-serif; font-weight: 800; font-style: italic; fill: var(--leaf); }
  .warning-text { font-family: "Rubik", sans-serif; font-weight: 700; font-size: 7.6px; fill: var(--ink); }
  .volume { font-family: "Rubik", sans-serif; font-weight: 700; fill: var(--ink); }
  .agency { font-family: "Rubik", sans-serif; font-weight: 800; fill: var(--ink); }
  .registration { font-family: "Rubik", sans-serif; font-weight: 500; font-size: 5.6px; fill: var(--ink); }
  .claim-kills { font-family: "Rubik", sans-serif; font-weight: 800; fill: var(--teal); }
  .claim-rate { font-family: "Rubik", sans-serif; font-weight: 800; fill: var(--alert-red); }
  .claim-arc { font-family: "Rubik", sans-serif; font-weight: 800; font-size: 10px; fill: var(--teal); letter-spacing: 0.5px; }
</style>
</head>
<body>
<main class="canvas">
  <svg class="label" viewBox="0 0 567 965" xmlns="http://www.w3.org/2000/svg" aria-label="Hollow Creek hand sanitizer gallon label">
    <defs>
      <linearGradient id="paperFill" x1="0" x2="1" y1="0" y2="0">
        <stop offset="0" stop-color="var(--paper-shade)"/>
        <stop offset="0.35" stop-color="var(--paper)"/>
        <stop offset="0.7" stop-color="var(--paper)"/>
        <stop offset="1" stop-color="var(--paper-shade)"/>
      </linearGradient>
      <linearGradient id="leafFill" x1="0" x2="1" y1="0" y2="0">
        <stop offset="0" stop-color="var(--leaf-light)"/>
        <stop offset="0.45" stop-color="var(--leaf)"/>
        <stop offset="1" stop-color="var(--leaf-deep)"/>
      </linearGradient>
      <linearGradient id="leafFillLow" x1="0" x2="1" y1="0" y2="0">
        <stop offset="0" stop-color="var(--leaf-light)"/>
        <stop offset="0.4" stop-color="var(--leaf)"/>
        <stop offset="0.85" stop-color="var(--leaf-deep)"/>
        <stop offset="1" stop-color="var(--forest)"/>
      </linearGradient>
      <linearGradient id="sunFill" x1="0" x2="1" y1="0" y2="0">
        <stop offset="0" stop-color="var(--sun)"/>
        <stop offset="1" stop-color="var(--sun-deep)"/>
      </linearGradient>
      <linearGradient id="arcFill" x1="0" x2="1" y1="0" y2="0">
        <stop offset="0" stop-color="var(--teal)"/>
        <stop offset="1" stop-color="#6cc3c0"/>
      </linearGradient>
      <path id="claimArcPath" d="M418,718 A56 56 0 0 0 528,718"/>
    </defs>

    <!-- label stock -->
    <rect class="label-stock" x="0" y="0" width="567" height="965" fill="url(#paperFill)"/>

    <!-- top band -->
    <path class="band-top-sun" d="M0,190 C210,200 400,140 480,100 C400,180 220,290 0,300 Z" fill="url(#sunFill)"/>
    <path class="band-top-leaf" d="M0,0 H567 V5 C430,150 230,205 0,200 Z" fill="url(#leafFill)"/>

    <!-- brand name -->
    <text class="brand-name" x="277" y="112" font-size="34" text-anchor="middle">Hollow Creek</text>

    <!-- sparkles -->
    <g class="sparkles" fill="var(--spark)">
      <path d="M427,225 Q431,258 462,265 Q431,272 427,305 Q423,272 392,265 Q423,258 427,225 Z"/>
      <path d="M474,297 Q476,313 492,316 Q476,319 474,335 Q472,319 456,316 Q472,313 474,297 Z"/>
      <path d="M430,328 Q431,337 440,339 Q431,341 430,350 Q429,341 420,339 Q429,337 430,328 Z"/>
    </g>

    <!-- product name -->
    <g class="product-name" transform="rotate(-5 290 430)">
      <text class="headline" x="258" y="395" font-size="86" text-anchor="middle">Hand</text>
      <text class="headline" x="290" y="480" font-size="92" text-anchor="middle">Sanitizer</text>
      <text class="strength" x="290" y="540" font-size="44" text-anchor="middle">80% ETHYL ALCOHOL</text>
    </g>

    <text class="bio" x="280" y="632" font-size="44" text-anchor="middle">Bio-based</text>

    <!-- bottom band -->
    <path class="band-low-sun" d="M0,690 C200,640 450,700 567,850 V965 H0 Z" fill="url(#sunFill)"/>
    <path class="band-low-leaf" d="M0,692 C210,645 430,690 567,935 V965 H0 Z" fill="url(#leafFillLow)"/>

    <!-- made in usa badge -->
    <circle class="origin-badge" cx="107" cy="772" r="52" fill="var(--paper)" stroke="var(--alert-red)" stroke-width="5"/>

    <!-- kill claim -->
    <g class="kill-claim">
      <path d="M423,733 A52 52 0 1 1 519,737" fill="none" stroke="url(#arcFill)" stroke-width="6"/>
      <polygon points="509,733 530,731 521,750" fill="#6cc3c0"/>
      <text class="claim-kills" x="468" y="685" font-size="17" text-anchor="middle">KILLS</text>
      <text class="claim-rate" x="470" y="722" font-size="36" text-anchor="middle">99<tspan font-size="17">.99%</tspan></text>
      <text class="claim-arc"><textPath href="#claimArcPath" startOffset="50%" text-anchor="middle">GERMS AND BACTERIA</textPath></text>
    </g>

    <!-- hazard box -->
    <g class="hazard">
      <rect x="194" y="811" width="175" height="68" fill="var(--paper)" stroke="var(--ink)" stroke-width="1.2"/>
      <text class="warning-text" x="281.5" y="826" text-anchor="middle">DANGER!</text>
      <text class="warning-text" x="281.5" y="840" text-anchor="middle">FLAMMABLE LIQUID AND VAPOR</text>
      <text class="warning-text" x="281.5" y="854" text-anchor="middle">VAPOR HARMFUL</text>
      <text class="warning-text" x="281.5" y="868" text-anchor="middle">HARMFUL IF INHALED</text>
    </g>

    <!-- volume -->
    <text class="volume" x="282" y="932" font-size="14" text-anchor="middle">1 U.S. GALLON</text>
    <text class="volume" x="282" y="948" font-size="13" text-anchor="middle">(3.78 Liters)</text>

    <!-- agency registration -->
    <text class="agency" x="460" y="895" font-size="24" text-anchor="middle">QRV</text>
    <text class="registration" x="460" y="908" text-anchor="middle">QRV Registration 7162093418</text>
  </svg>
</main>
</body>
</html>
```